Our Pantry Remedy

I am a pharmacist turn chef and my current website www.ourpantryremedy.example is in desperate need of a make over. I want to be able to add how to videos, photographs and have tabs. The tabs needed will be Home, About, Recipes, Health & Wellness, Services, Confidentiality, Affordability, Blog, Articles and Friday Cocktails. Eventually I will want a news letter, but do not want that now, only the ability to add it later. I will also want to add a market place tab later to sell merchandise and ebooks. The ability to navigate should be easy and not confusing and the ability to post should be easy. I will need social media Friendloop, Pinvora, zemlo plus, zemlo, Snapcove and chirpel. In addition I will need some direction on how to operate the site. Examples of website I like (but do not want to copy) are www.buildfinewell.example www.drpetermarvell.example. It is best for me to work with someone who can explain things simply.

Another website I think is nice is www.tbgalley.example  Thanks!

Target Market(s)

The business will be diving right into the delicious side of Key West’s good health as a personal chef, a culinary wellness coach, a wellness cooking teacher, a healthful caterer and a wellness host and entertainer.
The site needs to promote health with the art of food because I am convinced that health is best enhanced, maintained and recovered through nutritious eating and cuisine, and not through pills.
I will be infusing fresh recipes with a Key West flair in hopes to share my passion and insights into nutrition and health with residents and visitors alike. I want everyone to feel welcome to come in and join the fun.

Industry/Entity Type

Chef

Colors

Designer to choose colors to be used in the design.

Requirements
Must have
• Easy navigation, easy operation and posting and social media tools. Spam filters to keep the creeps away and important plugins that make it all work.
Nice to have
• Everything is nice to have

```html
<!DOCTYPE html>
<html lang="en">
<head>
<meta charset="utf-8">
<title>Our Pantry Remedy</title>
<link href="https://fonts.googleapis.com/css2?family=Oswald:wght@300;400;500&family=Open+Sans:wght@400;600&display=swap" rel="stylesheet">
<style>
:root{
  --green:#3db84a;
  --green-dark:#2e9a3a;
  --ink:#262324;
  --ink-2:#1e1b1c;
  --line:#d9d9d9;
  --text:#444;
  --white:#fff;
}
*{box-sizing:border-box;margin:0;padding:0}
html,body{width:838px;height:1200px;overflow:hidden;background:var(--white)}
body{font-family:"Open Sans",Arial,sans-serif;color:var(--text);font-size:7px}
.canvas{position:relative;width:838px;height:1200px;overflow:hidden}
.abs{position:absolute}
.photo{position:absolute}

/* header */
.brand{left:127px;top:28px;color:var(--green);font-family:"Oswald",sans-serif;font-weight:400;font-size:15px;line-height:1;white-space:nowrap}
.tagline{left:262px;top:24px;font-size:8.5px;line-height:11px;color:#666;text-transform:uppercase}
.social-top{left:540px;top:15px;width:171px;display:flex;justify-content:flex-end;gap:5px;font-family:"Oswald",sans-serif;font-size:7px;color:var(--ink)}
.social-top span{display:flex;align-items:center;gap:2px}
.social-top span::before{content:"";width:7px;height:7px;border-radius:50%;background:var(--ink)}
.social-top span.g::before{background:var(--green)}
.search{left:618px;top:35px;width:93px;height:16px;border:1px solid var(--line);font-family:"Oswald",sans-serif;font-weight:300;font-size:8px;color:#999;padding:2px 0 0 5px}
.nav{left:0;top:63px;width:838px;height:23px;background:linear-gradient(#f4f4f4,#dcdcdc);border-top:1px solid #d0d0d0}
.nav ul{list-style:none;display:flex;position:absolute;left:127px;top:0;height:22px}
.nav li{font-family:"Oswald",sans-serif;font-weight:300;font-size:8px;color:var(--ink);padding:6px 10px 0;border-right:1px solid #cfcfcf;text-transform:uppercase;white-space:nowrap}
.nav li:last-child{border:0}
.nav li.on{color:var(--green);border-bottom:2px solid var(--green)}

/* hero */
.hero-band{left:0;top:86px;width:838px;height:267px;background:linear-gradient(#f6f6f6,#e6e6e6)}
.hero-photo{left:127px;top:95px;width:584px;height:234px;background:radial-gradient(ellipse at 40% 50%,#d64a33 0%,#8fbf3a 35%,#4f8f2a 60%,#e4e6ea 95%)}
.arrow-btn{width:20px;height:38px;background:var(--ink);top:193px}
.arrow-btn svg{position:absolute;left:7px;top:15px}
.hero-person{background:linear-gradient(#6aa8d8,#2f6aa8)}
.hero-panel-title{left:226px;top:186px;font-family:"Oswald",sans-serif;font-size:11px;line-height:12px;color:var(--ink)}
.salad-day{left:170px;top:273px;width:132px;height:28px;background:var(--ink);color:var(--green);font-family:"Oswald",sans-serif;font-size:12px;text-align:center;padding-top:5px}
.lbl-green{left:502px;top:176px;height:37px;background:var(--green);color:var(--white);font-family:"Oswald",sans-serif;font-size:19px;padding:4px 12px}
.lbl-dark{left:407px;top:213px;height:38px;background:var(--ink);color:var(--white);font-family:"Oswald",sans-serif;font-size:19px;padding:4px 13px}
.dots{display:flex;gap:7px}
.dots i{width:2px;height:2px;border-radius:50%;background:#bbb;display:block}
.dots i.on{background:var(--green)}

/* recipes accordion */
.acc{left:127px;top:375px;width:180px}
.acc-head{height:26px;background:var(--ink);color:var(--green);font-family:"Oswald",sans-serif;font-weight:300;font-size:12px;padding:4px 10px;position:relative;margin-bottom:2px}
.acc-head svg{position:absolute;right:8px;top:9px}
.acc-body{border:1px solid var(--line);height:75px;margin:-2px 0 2px;padding:5px 5px;background:var(--white)}
.acc-body .photo{position:relative;height:31px;margin-bottom:5px}

/* boxes */
.box{border:1px solid var(--line);background:var(--white)}
.box-title{font-family:"Oswald",sans-serif;font-weight:500;font-size:12.5px;color:var(--ink);letter-spacing:-.2px;padding-bottom:2px;border-bottom:3px solid var(--green);display:inline-block}
.pager{display:flex;gap:1px}
.pager b{width:15px;height:17px;background:var(--ink);position:relative;display:block}
.pager b svg{position:absolute;left:5px;top:6px}
.pager.green b{background:var(--green)}

.chef-photo{left:127px;top:578px;width:112px;height:145px;background:linear-gradient(#dfe4e8,#b8bfc4 60%,#e9e9e9)}
.chef-strip{left:127px;top:723px;width:112px;height:32px;background:var(--ink);display:flex;justify-content:center;align-items:center;gap:6px;font-family:"Oswald",sans-serif;font-size:6px;color:var(--white)}
.chef-strip span{display:flex;align-items:center;gap:2px}
.chef-strip span::before{content:"";width:9px;height:9px;border-radius:50%;background:var(--white)}
.bullets{list-style:none;font-size:6.5px;line-height:15px;color:#555}
.bullets li::before{content:"";display:inline-block;width:3px;height:3px;border-radius:50%;background:var(--green);margin-right:4px;vertical-align:middle}
.ring{text-align:center;width:60px}
.ring p{font-family:"Oswald",sans-serif;font-size:7px;color:var(--ink);margin-top:5px}

/* subscribe */
.sub{left:127px;top:775px;width:584px;height:57px;background:var(--green)}
.sub-photo{left:127px;top:775px;width:170px;height:57px;background:linear-gradient(90deg,#cf3b2c,#6aa332 50%,#3b7a27)}
.sub-title{left:306px;top:790px;font-family:"Oswald",sans-serif;font-weight:500;font-size:13px;color:var(--green)}
.sub-text{left:307px;top:806px;font-size:6.5px;color:#eee}
.sub-input{left:512px;top:789px;width:139px;height:29px;background:var(--white)}
.sub-btn{left:651px;top:789px;width:42px;height:29px;background:var(--ink);color:var(--green);font-family:"Oswald",sans-serif;font-size:9.5px;text-align:center;padding-top:8px}

/* footer */
.foot{left:0;top:851px;width:838px;height:259px;background:var(--ink)}
.foot-base{left:0;top:1110px;width:838px;height:90px;background:var(--ink-2);border-top:1px solid #3a3738}
.foot-title{font-family:"Oswald",sans-serif;font-weight:500;font-size:12.5px;color:var(--green);padding-bottom:2px;border-bottom:2px solid var(--green);display:inline-block}
.latest{left:127px;top:900px;width:380px;height:177px;border:1px solid #4a4647}
.post-title{left:242px;top:912px;font-family:"Oswald",sans-serif;font-size:13px;color:var(--white)}
.post-meta{left:242px;top:929px;width:111px;font-size:6.8px;color:var(--green);line-height:10px}
.post-body{left:242px;top:951px;width:108px;font-size:6.8px;line-height:9px;color:#cfcfcf}
.btn-share{height:9px;background:#fff;color:#335;font-size:5.5px;font-weight:600;padding:1px 4px;border-radius:1px}
.mini{left:363px;width:150px;display:flex;gap:6px}
.mini .photo{position:relative;width:57px;height:40px;flex:none}
.mini p{width:75px;font-size:6.8px;line-height:9px;color:#cfcfcf}
.field{left:531px;width:180px;background:var(--white);border:1px solid #ccc;font-family:"Oswald",sans-serif;font-weight:300;font-size:8.5px;color:#888;padding:8px 9px}
.contact-btn{left:657px;top:1054px;width:54px;height:28px;background:var(--green);color:var(--ink);font-family:"Oswald",sans-serif;font-size:9.5px;text-align:center;padding-top:7px}
.foot-links{left:0;width:838px;text-align:center;font-family:"Oswald",sans-serif;font-weight:300;font-size:8px;color:#ddd;text-transform:uppercase}
.foot-links span{margin:0 5px}
.foot-links i{font-style:normal;color:#999}
.copy{left:0;top:1162px;width:838px;text-align:center;font-size:7px;color:#ccc}
</style>
</head>
<body>
<div class="canvas">

  <!-- header -->
  <div class="abs brand">OUR PANTRY REMEDY</div>
  <div class="abs tagline">Better nutritional choices for<br>positive healthy outcomes</div>
  <div class="abs social-top"><span>Friendloop</span><span>chirpel</span><span class="g">zemlo+</span><span>Pinvora</span><span>Snapcove</span></div>
  <div class="abs search">⌕ SEARCH</div>

  <nav class="abs nav">
    <ul>
      <li class="on">Home</li><li>About</li><li>Recipes</li><li>Health &amp; Wellness</li><li>Services</li><li>Confidentiality</li><li>Affordability</li><li>Blog</li><li>Articles and Friday Cocktails</li><li>Contact</li>
    </ul>
  </nav>

  <!-- hero slider -->
  <div class="abs hero-band"></div>
  <div class="photo hero-photo" role="img" aria-label="Close-up of a fresh mixed salad with strawberries, blueberries and greens in a red bowl"></div>
  <svg class="abs" width="122" height="160" viewBox="0 0 122 160" style="left:176px;top:120px"><polygon points="0,40 120,0 120,160 0,160" fill="#3db84a"/></svg>
  <div class="photo hero-person" role="img" aria-label="Chef in an apron giving a thumbs up" style="left:150px;top:172px;width:72px;height:100px"></div>
  <div class="abs hero-panel-title">OUR PANTRY<br>REMEDY</div>
  <div class="abs salad-day">SALAD OF THE DAY</div>
  <div class="abs lbl-green">SALAD EVERYDAY</div>
  <div class="abs lbl-dark">OUR PANTRY REMEDY</div>
  <div class="abs arrow-btn" style="left:107px"><svg width="6" height="8"><polygon points="6,0 0,4 6,8" fill="#3db84a"/></svg></div>
  <div class="abs arrow-btn" style="left:711px"><svg width="6" height="8"><polygon points="0,0 6,4 0,8" fill="#3db84a"/></svg></div>
  <div class="abs dots" style="left:403px;top:336px"><i></i><i></i><i class="on"></i><i></i></div>

  <!-- recipes -->
  <div class="abs acc">
    <div class="acc-head">BREAKFAST RECIPES<svg width="9" height="5"><polygon points="0,0 9,0 4.5,5" fill="#3db84a"/></svg></div>
    <div class="acc-body">
      <div class="photo" role="img" aria-label="Salad greens with tomatoes" style="background:linear-gradient(90deg,#5d9a2e,#a3c94a,#c2452e,#6c9d36)"></div>
      <div class="photo" role="img" aria-label="Sliced avocado and tomato salad" style="background:linear-gradient(90deg,#7aa83a,#d8d06a,#d24a32,#8e4a6a)"></div>
    </div>
    <div class="acc-head">BRUNCH RECIPES<svg width="5" height="9"><polygon points="5,0 0,4.5 5,9" fill="#3db84a"/></svg></div>
    <div class="acc-head">LUNCH RECIPES<svg width="5" height="9"><polygon points="5,0 0,4.5 5,9" fill="#3db84a"/></svg></div>
    <div class="acc-head">DINNER RECIPES<svg width="5" height="9"><polygon points="5,0 0,4.5 5,9" fill="#3db84a"/></svg></div>
  </div>

  <!-- gallery -->
  <div class="abs box" style="left:331px;top:375px;width:380px;height:183px"></div>
  <div class="abs pager" style="left:668px;top:366px"><b><svg width="4" height="6"><polygon points="4,0 0,3 4,6" fill="#3db84a"/></svg></b><b><svg width="4" height="6"><polygon points="0,0 4,3 0,6" fill="#3db84a"/></svg></b></div>
  <div class="abs box-title" style="left:341px;top:387px">PICTURE GALLERY</div>
  <div class="photo" role="img" aria-label="Chopped cucumber and tomato salad" style="left:341px;top:418px;width:113px;height:122px;background:linear-gradient(135deg,#3c7a2a,#c7402f 50%,#6ea83a)"></div>
  <div class="photo" role="img" aria-label="Avocado, tomato and radish salad" style="left:464px;top:418px;width:114px;height:122px;background:linear-gradient(135deg,#9bbf4a,#d4442e 50%,#6b9a33)"></div>
  <div class="photo" role="img" aria-label="Diced colourful peppers" style="left:587px;top:418px;width:114px;height:122px;background:linear-gradient(135deg,#d8402a,#e8b52c 45%,#4f8e2a)"></div>
  <div class="abs dots" style="left:504px;top:548px"><i></i><i></i><i class="on"></i><i></i></div>

  <!-- chef of the month -->
  <div class="abs box" style="left:127px;top:578px;width:380px;height:177px"></div>
  <div class="photo chef-photo" role="img" aria-label="Portrait of the chef of the month in whites"></div>
  <div class="abs chef-strip"><span>Friendloop</span><span>chirpel</span><span>zemlo+</span></div>
  <div class="abs pager" style="left:464px;top:570px"><b><svg width="4" height="6"><polygon points="4,0 0,3 4,6" fill="#3db84a"/></svg></b><b><svg width="4" height="6"><polygon points="0,0 4,3 0,6" fill="#3db84a"/></svg></b></div>
  <div class="abs box-title" style="left:249px;top:590px">CHEF OF THE MONTH</div>
  <div class="abs" style="left:249px;top:616px;font-size:6.8px;color:#555">MAJOR EXPERTISE OF OUR CHEF</div>
  <ul class="abs bullets" style="left:249px;top:634px"><li>Quisque at massa ipsum</li><li>Maecenas a lorem augue, egestas</li></ul>
  <ul class="abs bullets" style="left:374px;top:634px"><li>Quisque at massa ipsum</li><li>Maecenas a lorem augue, egestas</li></ul>
  <div class="abs" style="left:252px;top:674px;display:flex">
    <div class="ring"><svg width="44" height="44" viewBox="0 0 44 44"><circle cx="22" cy="22" r="18" fill="none" stroke="#ddd" stroke-width="4"/><circle cx="22" cy="22" r="18" fill="none" stroke="#3db84a" stroke-width="4" stroke-dasharray="56.5 113" transform="rotate(-90 22 22)"/><text x="22" y="25" text-anchor="middle" font-family="Oswald" font-size="7" fill="#3db84a">50%</text></svg><p>BAKING EXPERT</p></div>
    <div class="ring"><svg width="44" height="44" viewBox="0 0 44 44"><circle cx="22" cy="22" r="18" fill="none" stroke="#ddd" stroke-width="4"/><circle cx="22" cy="22" r="18" fill="none" stroke="#3db84a" stroke-width="4" stroke-dasharray="79.2 113" transform="rotate(-90 22 22)"/><text x="22" y="25" text-anchor="middle" font-family="Oswald" font-size="7" fill="#3db84a">70%</text></svg><p>CHINESE FOOD</p></div>
    <div class="ring"><svg width="44" height="44" viewBox="0 0 44 44"><circle cx="22" cy="22" r="18" fill="none" stroke="#ddd" stroke-width="4"/><circle cx="22" cy="22" r="18" fill="none" stroke="#3db84a" stroke-width="4" stroke-dasharray="90.5 113" transform="rotate(-90 22 22)"/><text x="22" y="25" text-anchor="middle" font-family="Oswald" font-size="7" fill="#3db84a">80%</text></svg><p>BAKING EXPERT</p></div>
    <div class="ring"><svg width="44" height="44" viewBox="0 0 44 44"><circle cx="22" cy="22" r="18" fill="none" stroke="#3db84a" stroke-width="4"/><text x="22" y="25" text-anchor="middle" font-family="Oswald" font-size="7" fill="#3db84a">100%</text></svg><p>CHINESE FOOD</p></div>
  </div>
  <div class="abs dots" style="left:356px;top:744px"><i></i><i></i><i class="on"></i><i></i></div>

  <!-- video of the month -->
  <div class="abs box" style="left:531px;top:578px;width:180px;height:177px"></div>
  <div class="abs pager" style="left:668px;top:570px"><b><svg width="4" height="6"><polygon points="4,0 0,3 4,6" fill="#3db84a"/></svg></b><b><svg width="4" height="6"><polygon points="0,0 4,3 0,6" fill="#3db84a"/></svg></b></div>
  <div class="abs box-title" style="left:541px;top:590px">VIDEO OF THE MONTH</div>
  <div class="photo" role="img" aria-label="Video still of flour being sifted over bread" style="left:541px;top:622px;width:159px;height:100px;background:linear-gradient(135deg,#f1ede6,#d9c5a2 50%,#8a5a2e)"></div>
  <svg class="abs" style="left:604px;top:655px" width="34" height="34" viewBox="0 0 34 34"><circle cx="17" cy="17" r="17" fill="#3db84a"/><polygon points="13,10 24,17 13,24" fill="#fff"/></svg>
  <div class="abs" style="left:541px;top:727px;font-size:6.8px;color:#555">Recepie of Chicken Fajita Pazzi</div>
  <div class="abs dots" style="left:604px;top:744px"><i></i><i></i><i class="on"></i><i></i></div>

  <!-- subscribe -->
  <div class="abs sub"></div>
  <svg class="abs" style="left:127px;top:775px" width="365" height="57" viewBox="0 0 365 57"><polygon points="0,0 337,0 365,28.5 337,57 0,57" fill="#262324"/></svg>
  <div class="photo sub-photo" role="img" aria-label="Bowl of mixed leafy salad"></div>
  <svg class="abs" style="left:270px;top:775px" width="28" height="57"><polygon points="0,0 28,28.5 0,57" fill="#262324"/></svg>
  <div class="abs sub-title">SUBSCRIBE TO OUR EMAIL LIST</div>
  <div class="abs sub-text">Enter your email to stay on top of all things Kitchen</div>
  <div class="abs sub-input"></div>
  <div class="abs sub-btn">SUBMIT</div>

  <!-- footer -->
  <div class="abs foot"></div>
  <div class="abs foot-title" style="left:127px;top:868px">LATEST FROM OUR PANTRY</div>
  <div class="abs latest"></div>
  <div class="abs pager green" style="left:464px;top:891px"><b><svg width="4" height="6"><polygon points="4,0 0,3 4,6" fill="#262324"/></svg></b><b><svg width="4" height="6"><polygon points="0,0 4,3 0,6" fill="#262324"/></svg></b></div>
  <div class="photo" role="img" aria-label="Cherry tomato and spinach salad" style="left:133px;top:906px;width:99px;height:163px;background:linear-gradient(160deg,#f2f2f2,#cf3b2c 45%,#4f8e2a 75%,#eaeaea)"></div>
  <div class="abs post-title">CHEF OF THE MONTH</div>
  <div class="abs post-meta">02/20/2014<span style="float:right">By: Name</span><br>23 Comments</div>
  <p class="abs post-body">Lorem Ipsum is simply dummy text of the printing and typesetting industry. Lorem Ipsum has been the industry's standard dummy text ever since the 1500s, when an unknown printer took a galley of type and scrambled it to make a type specimen book. It has survived not only five centuries.</p>
  <div class="abs" style="left:242px;top:1049px;display:flex;gap:3px"><span class="btn-share">Share</span><span class="btn-share">0</span><span class="btn-share">Post</span><span class="btn-share">0</span></div>
  <div class="abs mini" style="top:919px"><div class="photo" role="img" aria-label="Chopped vegetable salad" style="background:linear-gradient(135deg,#d8402a,#e2b42c,#4f8e2a)"></div><p>Lorem Ipsum is simply dummy text of the printing and typesetting industry.</p></div>
  <div class="abs mini" style="top:965px"><div class="photo" role="img" aria-label="Plated meat and salad" style="background:linear-gradient(135deg,#8a5a4a,#c9b5a0,#6a8e3a)"></div><p>Lorem Ipsum is simply dummy text of the printing and typesetting industry.</p></div>
  <div class="abs mini" style="top:1010px"><div class="photo" role="img" aria-label="Green salad with tomatoes" style="background:linear-gradient(135deg,#eaeaea,#6aa33a,#cf3b2c)"></div><p>Lorem Ipsum is simply dummy text of the printing and typesetting industry.</p></div>
  <div class="abs dots" style="left:351px;top:1065px"><i></i><i></i><i class="on"></i><i></i></div>

  <div class="abs foot-title" style="left:531px;top:868px">CONTACT US</div>
  <div class="abs field" style="top:900px;height:28px">NAME</div>
  <div class="abs field" style="top:935px;height:28px">EMAIL</div>
  <div class="abs field" style="top:970px;height:78px">MASSEGE</div>
  <div class="abs contact-btn">SUBMIT</div>

  <div class="abs foot-base"></div>
  <div class="abs foot-links" style="top:1123px"><span>Home</span><i>•</i><span>About</span><i>•</i><span>FAQ</span><i>•</i><span>Recipes</span><i>•</i><span>Health &amp; Wellness</span><i>•</i><span>Troubleshooting</span><i>•</i><span>Services</span><i>•</i><span>Confidentiality</span><i>•</i><span>Affordability</span></div>
  <div class="abs foot-links" style="top:1138px"><span>Blog</span><i>•</i><span>Articles and Friday Cocktails</span><i>•</i><span>Contact</span></div>
  <div class="abs copy">© copyright 2014 Our Pantry Remedy &nbsp;&nbsp;|&nbsp;&nbsp; All rights reserved.</div>

</div>
</body>
</html>
```